HomeBridle business card and stationary design

We are looking for a simple yet elegant design for our mortgage company business card and stationary.

The card should include:
Name (Derek Walsh)
Title (CEO)
Phone Number (614-208-3917)
Address (48 Birchfield Court, Suite 314, Marlow, OH 43952)
Email (email@homebridle-example.com)
"NMLS" i.e. (NMLS 61947)
"Company NMLS" (Company NMLS 472815)

See above

```html
<!DOCTYPE html>
<html lang="en">
<head>
<meta charset="utf-8">
<title>HomeBridle Business Card</title>
<link rel="stylesheet" href="https://fonts.googleapis.com/css2?family=Montserrat:wght@400;500;700;800&display=swap">
<style>
  :root {
    --bg: #4a4d52;
    --card: #ffffff;
    --brand-blue: #29abe2;
    --navy: #1a2533;
    --ink: #111417;
  }
  * { box-sizing: border-box; margin: 0; padding: 0; }
  html, body {
    width: 1200px; height: 887px; overflow: hidden;
    background: var(--bg);
    font-family: "Montserrat", Arial, sans-serif;
  }
  .canvas { position: relative; width: 1200px; height: 887px; }

  .card {
    position: absolute;
    width: 580px; height: 331px;
    background: var(--card);
    border-radius: 26px;
    overflow: hidden;
    box-shadow: 0 10px 24px rgba(0,0,0,0.35);
  }
  .card--front { left: 70px; top: 70px; }
  .card--back  { left: 550px; top: 486px; }

  .wordmark {
    display: flex; align-items: center; gap: 10px;
    font-weight: 700; color: var(--brand-blue);
    letter-spacing: 0.5px; white-space: nowrap;
  }
  .wordmark__dot { width: 12px; height: 12px; background: var(--brand-blue); border-radius: 50%; flex: none; }

  .card--front .wordmark {
    position: absolute; left: 50%; top: 50%;
    transform: translate(-50%, -50%);
    font-size: 58px; gap: 12px;
  }
  .card--front .wordmark__dot { width: 22px; height: 22px; }

  .back-logo-area {
    position: absolute; left: 0; top: 52px;
    width: 270px; height: 150px;
    display: flex; align-items: center; justify-content: center;
  }
  .card--back .wordmark { font-size: 29px; }

  .divider {
    position: absolute; left: 282px; top: 52px;
    width: 2px; height: 150px; background: var(--brand-blue);
  }

  .details { position: absolute; left: 304px; top: 44px; color: var(--ink); }
  .details__name {
    font-size: 17px; font-weight: 800; color: var(--brand-blue);
    text-transform: uppercase; letter-spacing: 0.3px;
  }
  .details__title { font-size: 13px; font-weight: 800; margin: 2px 0 12px 14px; }
  .details__license { font-size: 11.5px; font-weight: 500; line-height: 1.45; margin-left: 14px; }
  .contact { list-style: none; margin-top: 10px; margin-left: 14px; }
  .contact li {
    display: flex; align-items: center; gap: 8px;
    font-size: 11.5px; font-weight: 500; line-height: 1.9;
  }
  .contact svg { width: 13px; height: 13px; flex: none; }

  .address-band {
    position: absolute; left: 0; right: 0; top: 236px; height: 68px;
    background: var(--navy);
    display: flex; align-items: center; justify-content: center;
    color: #ffffff; font-size: 14px; font-weight: 500; letter-spacing: 0.3px;
  }
</style>
</head>
<body>
<div class="canvas">

  <section class="card card--front" aria-label="Card front">
    <div class="wordmark"><span class="wordmark__dot"></span><span>HomeBridle</span></div>
  </section>

  <section class="card card--back" aria-label="Card back">
    <div class="back-logo-area">
      <div class="wordmark"><span class="wordmark__dot"></span><span>HomeBridle</span></div>
    </div>
    <div class="divider"></div>

    <div class="details">
      <p class="details__name">Derek Walsh</p>
      <p class="details__title">CEO</p>
      <p class="details__license">"NMLS" i.e. (NMLS 61947)<br>Company NMLS 472815</p>
      <ul class="contact">
        <li>
          <svg viewBox="0 0 16 16" aria-hidden="true"><path fill="var(--brand-blue)" d="M3.6 1.5l2.3 2.6-1.3 1.6c.9 2 2.5 3.6 4.5 4.5l1.6-1.3 2.6 2.3-1.4 2.3C6.8 13.3 2.7 9.2 1.5 4.1z"/></svg>
          614-208-3917
        </li>
        <li>
          <svg viewBox="0 0 16 16" aria-hidden="true"><rect x="1" y="3" width="14" height="10" rx="1" fill="var(--brand-blue)"/><path d="M1.5 3.8L8 9l6.5-5.2" fill="none" stroke="#fff" stroke-width="1.3"/></svg>
          email@homebridle-example.com
        </li>
        <li>
          <svg viewBox="0 0 16 16" aria-hidden="true"><circle cx="8" cy="8" r="7" fill="var(--brand-blue)"/><path d="M1 8h14M8 1c-3 3-3 11 0 14M8 1c3 3 3 11 0 14" fill="none" stroke="#fff" stroke-width="1"/></svg>
          www.homebridle.com
        </li>
      </ul>
    </div>

    <div class="address-band">48 Birchfield Court, Suite 314, Marlow, OH 43952</div>
  </section>

</div>
</body>
</html>
```